Need Letterhead Design & Matching Business Card

I have a logo that I love already. But the letterhead is less than appealing and boring. I'd like a design for my letterhead which I will match with business cards. Also, I'd like to have used fonts that are generally available, as my current letterhead uses a font named "SPACE" which nobody has unless they download it...so when a Word version is forwarded, it looks awful on the receiver's screed due to not having the font. That being said, modern is the look we like and are going for.

My business is "Halloran Brightmoor PC" - a law firm specializing in representing people who have suffered catastrophic injuries or death (plane, auto, train crashes etc.).

See attached letterhead, which has all of the pertinent information. My logo is also attached in various formats.

```html
<!DOCTYPE html>
<html lang="en">
<head>
<meta charset="utf-8">
<title>Halloran Brightmoor PC — Letterhead</title>
<link rel="stylesheet" href="https://fonts.googleapis.com/css2?family=Montserrat:wght@400;500;600&display=swap">
<style>
  :root {
    --backdrop: #e9e9ea;
    --paper: #f7f7f6;
    --ink: #2b2b2d;
    --ink-soft: #4a4a4d;
    --mark: #2a2a2c;
    --band: #ececeb;
    --signature: #e3e6f4;
    --rule: #3a3a3c;
  }
  * { box-sizing: border-box; margin: 0; padding: 0; }
  html, body { width: 1200px; height: 900px; overflow: hidden; }
  body {
    background: var(--backdrop);
    font-family: "Montserrat", sans-serif;
    color: var(--ink);
    position: relative;
  }
  .letterhead {
    position: absolute;
    left: 300px;
    top: 26px;
    width: 600px;
    height: 848px;
    background: var(--paper);
    box-shadow: 0 2px 10px rgba(0,0,0,0.08);
  }
  .brand {
    position: absolute;
    left: 64px;
    top: 80px;
    display: flex;
    align-items: center;
    gap: 12px;
  }
  .brand-square {
    width: 38px;
    height: 38px;
    background: var(--mark);
  }
  .brand-name {
    font-size: 15px;
    font-weight: 400;
    letter-spacing: 0.14em;
    color: var(--ink);
  }
  .edge-band {
    position: absolute;
    right: 0;
    top: 0;
    width: 56px;
    height: 560px;
    background: var(--band);
  }
  .letter-body {
    position: absolute;
    left: 64px;
    top: 200px;
    width: 400px;
    font-size: 9.5px;
    line-height: 1.6;
    color: var(--ink-soft);
  }
  .letter-body p + p { margin-top: 13px; }
  .sign-off {
    position: absolute;
    left: 64px;
    top: 530px;
  }
  .signature {
    width: 150px;
    height: 42px;
    background: var(--signature);
    border-radius: 3px;
  }
  .sign-role {
    margin-top: 4px;
    font-size: 9.5px;
    color: var(--ink-soft);
  }
  .footer {
    position: absolute;
    left: 64px;
    bottom: 60px;
    display: flex;
    gap: 40px;
  }
  .footer-block {
    border-left: 1px solid var(--rule);
    padding-left: 12px;
    font-size: 8.5px;
    font-weight: 500;
    line-height: 1.55;
    color: var(--ink);
  }
</style>
</head>
<body>
  <main class="letterhead">
    <header class="brand">
      <span class="brand-square" aria-hidden="true"></span>
      <span class="brand-name">HALLORAN BRIGHTMOOR</span>
    </header>

    <div class="edge-band" role="img" aria-label="Faint decorative pattern band along the right edge"></div>

    <section class="letter-body">
      <p>Thank you for considering our firm. We understand that the weeks after a serious accident are overwhelming, and our aim is to make the path ahead clearer. This letter sets out how we approach each matter, what you can expect from our team, and how we will keep you informed at every stage of your claim.</p>
      <p>Every case begins with a careful review of the facts, records and witness accounts. Our attorneys work alongside trusted experts to build a complete picture of what happened and why. We handle communication with insurers and opposing counsel so that you and your family can focus on recovery, rest and the people who matter most.</p>
      <p>Please reach out whenever a question arises, large or small. We will respond promptly and plainly, and we will never ask you to face this process alone. We look forward to working with you and to seeing this matter through to a fair and lasting resolution.</p>
    </section>

    <div class="sign-off">
      <div class="signature" role="img" aria-label="Handwritten signature in blue ink"></div>
      <p class="sign-role">company director</p>
    </div>

    <footer class="footer">
      <div class="footer-block">
        R. Tomas Ferrand, Esq. | President<br>
        4120 Larkspur Ave. | Suite 800<br>
        Fairhaven, CA 90388
      </div>
      <div class="footer-block">
        tomas@halloranbrightmoor.com<br>
        www.halloranbrightmoor.com<br>
        tel: (855) 555 0142
      </div>
    </footer>
  </main>
</body>
</html>
```